innovative investment real estate sales firm

We are a uniquely collabrative firm that seeks to bring a conultative approach to uncovering hidden opportunities for our clients, our website needs to convey our client focused approach. Our firm specializes in the sale of apartment properties in Southern California. We have a team of researchers, transaction coordinators and marketing personal to support our geographically specialized advisers. We need a website that introduces clients to our unique way of better helping them achieve their investment goals.

Target Market(s)

High net worth individuals and families

Industry/Entity Type

Real Estate Agent

Font styles to use
Other font styles liked:
• please use font provided

Requirements
Must have
• Stories of our recent projects
• Features on our people
• email capture for viewing inventory
• content that showcases our unique consultative approach that uncovers unrealized opportunities

```html
<!DOCTYPE html>
<html lang="en">
<head>
<meta charset="utf-8">
<title>Meridian Crest Advisers – Multifamily Properties</title>
<link href="https://fonts.googleapis.com/css2?family=Montserrat:wght@400;500;600;700&family=Open+Sans:wght@400;600&display=swap" rel="stylesheet">
<style>
  :root {
    --teal: #0ea5b8;
    --green: #8ccc0a;
    --slate: #3f4a55;
    --grey: #7c8287;
    --text: #3a4148;
    --body: #6b7177;
    --light: #f0f0f0;
    --card: #f2f2f2;
    --line: #d6d6d6;
    --white: #ffffff;
  }
  * { box-sizing: border-box; margin: 0; padding: 0; }
  html, body { width: 674px; height: 1200px; overflow: hidden; }
  body { position: relative; background: var(--white); font-family: "Open Sans", Arial, sans-serif; color: var(--text); }
  .abs { position: absolute; }

  /* header */
  .topbar { left: 0; top: 0; width: 674px; height: 68px; background: linear-gradient(180deg, #eef2f6, #e1e8ef); }
  .brand { left: 58px; top: 17px; display: flex; align-items: center; gap: 9px; }
  .brand-square { width: 30px; height: 30px; background: var(--teal); }
  .brand-name { font-family: "Montserrat", Arial, sans-serif; font-weight: 600; font-size: 14px; letter-spacing: 1.6px; color: var(--slate); line-height: 1.15; }
  .brand-tag { display: block; font-size: 5px; letter-spacing: 1.6px; color: var(--teal); font-weight: 500; margin-top: 2px; }
  .call { left: 470px; top: 28px; font-family: "Montserrat", Arial, sans-serif; font-size: 11.5px; font-weight: 500; color: var(--slate); display: flex; align-items: center; gap: 5px; }
  .navbar { left: 0; top: 68px; width: 674px; height: 32px; background: #e3e9f0; border-top: 1px solid #d3dbe4; }
  .nav { left: 78px; top: 79px; display: flex; font-family: "Montserrat", Arial, sans-serif; font-size: 7.6px; font-weight: 500; color: var(--slate); }
  .nav a { text-decoration: none; color: inherit; margin-right: 18px; }
  .nav a.active { color: var(--teal); }
  .search { left: 596px; top: 72px; width: 23px; height: 23px; border: 1.5px solid var(--teal); border-radius: 50%; display: flex; align-items: center; justify-content: center; }

  /* hero */
  .hero { left: 0; top: 100px; width: 674px; height: 252px;
    background:
      linear-gradient(90deg, rgba(60,90,130,.35) 0%, rgba(120,80,60,.25) 30%, rgba(90,120,160,.3) 50%, rgba(0,0,0,0) 70%),
      linear-gradient(180deg, #c9d8e6 0%, #a9c0d6 22%, #6f8fae 45%, #8a7d70 68%, #b8aa98 82%, #7f8a78 100%); }
  .hero-prev { left: 66px; top: 196px; }
  .hero-next { left: 592px; top: 190px; width: 27px; height: 28px; background: rgba(80,88,96,.75); display: flex; align-items: center; justify-content: center; }
  .hero-badge { left: 313px; top: 314px; width: 48px; height: 48px; border-radius: 50%; background: var(--teal); border: 2px solid var(--white); }

  /* section headings */
  .section-title { left: 0; width: 674px; display: flex; justify-content: center; align-items: center; gap: 8px; font-family: "Montserrat", Arial, sans-serif; font-weight: 600; font-size: 12.5px; letter-spacing: 2.8px; color: var(--slate); }
  .bars { display: flex; flex-direction: column; gap: 1.5px; }
  .bars i { display: block; width: 8px; height: 3px; }
  .bars i:nth-child(1) { background: var(--teal); }
  .bars i:nth-child(2) { background: var(--slate); }
  .bars i:nth-child(3) { background: var(--green); }

  .welcome-sub { left: 0; top: 414px; width: 674px; text-align: center; font-family: "Montserrat", Arial, sans-serif; font-weight: 600; font-size: 9px; color: var(--slate); }
  .welcome-text { left: 97px; top: 434px; width: 480px; text-align: center; font-size: 7.2px; line-height: 11.7px; color: var(--body); }
  .btn-read { left: 308px; top: 484px; width: 58px; height: 18px; background: var(--teal); color: var(--white); font-family: "Montserrat", Arial, sans-serif; font-size: 6.3px; font-weight: 600; display: flex; align-items: center; justify-content: center; }

  /* projects */
  .project { background: var(--card); border: 1px solid var(--line); box-shadow: 0 1px 2px rgba(0,0,0,.08); }
  .project-photo { width: 100%; }
  .project-body { padding: 8px 7px 0; }
  .project-name { font-family: "Montserrat", Arial, sans-serif; font-size: 8.6px; font-weight: 600; letter-spacing: 1.8px; color: var(--slate); margin-bottom: 3px; }
  .project-text { font-size: 6px; line-height: 10.8px; color: var(--body); text-align: justify; }
  .slider-btn { width: 27px; height: 29px; background: var(--slate); display: flex; align-items: center; justify-content: center; }

  /* people */
  .person { width: 123px; height: 165px; border: 1px solid var(--line); overflow: hidden; box-shadow: 0 1px 2px rgba(0,0,0,.1); }
  .person-photo { width: 100%; height: 132px; }
  .person-name { height: 33px; display: flex; align-items: center; justify-content: center; font-family: "Montserrat", Arial, sans-serif; font-weight: 600; font-size: 11.5px; letter-spacing: 2.5px; color: var(--white); }
  .person-bio { left: 8px; top: 20px; width: 107px; text-align: center; font-size: 5.6px; line-height: 11.6px; color: var(--white); }
  .person-social { left: 25px; top: 100px; display: flex; gap: 7px; }
  .person-social span { width: 14px; height: 14px; border-radius: 2px; display: flex; align-items: center; justify-content: center; }

  /* newsletter */
  .newsletter { left: 0; top: 1015px; width: 674px; height: 115px; background: var(--light); }
  .email-field { left: 187px; top: 1075px; width: 197px; height: 20px; background: var(--white); display: flex; align-items: center; justify-content: space-between; padding: 0 10px 0 14px; font-family: "Montserrat", Arial, sans-serif; font-size: 6px; letter-spacing: 1.5px; color: #a9aeb3; }
  .btn-subscribe { left: 391px; top: 1075px; width: 97px; height: 20px; background: var(--green); color: var(--white); font-family: "Montserrat", Arial, sans-serif; font-weight: 600; font-size: 9.5px; display: flex; align-items: center; justify-content: center; }

  /* footer */
  .footer-brand { left: 70px; top: 1150px; display: flex; align-items: center; gap: 6px; }
  .footer-brand .brand-square { width: 18px; height: 18px; }
  .footer-brand .brand-name { font-size: 7.5px; letter-spacing: 1px; }
  .footer-links { left: 293px; top: 1144px; display: flex; gap: 15px; font-family: "Montserrat", Arial, sans-serif; font-size: 7px; font-weight: 500; color: var(--slate); }
  .footer-copy { left: 452px; top: 1164px; font-size: 5.6px; font-weight: 600; color: var(--slate); }
</style>
</head>
<body>

<header>
  <div class="abs topbar"></div>
  <div class="abs brand">
    <span class="brand-square"></span>
    <span class="brand-name">MERIDIAN CREST<br>ADVISERS<span class="brand-tag">MULTIFAMILY PROPERTIES</span></span>
  </div>
  <div class="abs call">
    <svg width="10" height="10" viewBox="0 0 10 10"><rect width="10" height="10" rx="2" fill="#0ea5b8"/><path d="M3 2.3l1 1.2-.6.8c.4.9 1.1 1.6 2 2l.8-.6 1.2 1-.6 1c-2.6-.3-4.4-2.2-4.7-4.8z" fill="#fff"/></svg>
    Call Us : 1-800 555 0142
  </div>
  <div class="abs navbar"></div>
  <nav class="abs nav">
    <a class="active">HOME</a><a>ABOUT US</a><a>RECENT PROJECTS</a><a>OUR PEOPLE</a><a>SUBSCRIBE</a><a>CONTACT US</a>
  </nav>
  <div class="abs search">
    <svg width="10" height="10" viewBox="0 0 10 10"><circle cx="4.2" cy="4.2" r="3" fill="none" stroke="#0ea5b8" stroke-width="1.5"/><path d="M6.4 6.4L9 9" stroke="#0ea5b8" stroke-width="1.6"/></svg>
  </div>
</header>

<section>
  <div class="abs hero" role="img" aria-label="Downtown city skyline with glass towers under a cloudy blue sky"></div>
  <div class="abs hero-prev"><svg width="10" height="14" viewBox="0 0 10 14"><path d="M7 2L2 7l5 5" fill="none" stroke="#fff" stroke-width="1.6"/></svg></div>
  <div class="abs hero-next"><svg width="10" height="14" viewBox="0 0 10 14"><path d="M3 2l5 5-5 5" fill="none" stroke="#fff" stroke-width="1.6"/></svg></div>
  <div class="abs hero-badge"></div>
</section>

<section>
  <h1 class="abs section-title" style="top:389px;"><span class="bars"><i></i><i></i><i></i></span>WELCOME TO MERIDIAN CREST ADVISERS<span class="bars"><i></i><i></i><i></i></span></h1>
  <p class="abs welcome-sub">Sed ut perspiciatis unde omnis iste natus error sit voluptatem...</p>
  <p class="abs welcome-text">Sed ut perspiciatis unde omnis iste natus error sit voluptatem accusantium doloremque laudantium, totam rem aperiam, eaque ipsa quae ab illo inventore veritatis et quasi architecto beatae vitae dicta sunt explicabo. Nemo enim ipsam voluptatem quia voluptas sit aspernatur aut odit aut fugit, sed quia consequuntur magni dolores eos qui ratione voluptatem...</p>
  <div class="abs btn-read">READ MORE</div>
</section>

<section>
  <h2 class="abs section-title" style="top:532px;"><span class="bars"><i></i><i></i><i></i></span>RECENT PROJECTS<span class="bars"><i></i><i></i><i></i></span></h2>

  <article class="abs project" style="left:66px; top:571px; width:168px; height:174px;">
    <div class="project-photo" role="img" aria-label="Modern white apartment building with balconies against blue sky" style="height:109px; background:linear-gradient(120deg,#2a62c2 0%,#4f86d6 35%,#e6e2da 55%,#c9b9a4 75%,#6e5e4e 100%);"></div>
    <div class="project-body"><div class="project-name">PROJECT NAME</div><p class="project-text">Duis aute irure dolor in reprehenderit in voluptate velit esse cillum dolore eu fugiat nulla pariatur. Excepteur sint occaecat ....</p></div>
  </article>
  <article class="abs project" style="left:441px; top:571px; width:168px; height:174px;">
    <div class="project-photo" role="img" aria-label="Upward view of orange and white high-rise towers with clouds" style="height:109px; background:linear-gradient(135deg,#d96a34 0%,#e8a37c 20%,#9ec1ea 42%,#f3f6fa 58%,#8fb7e6 70%,#ef7a3a 88%,#f0eeea 100%);"></div>
    <div class="project-body"><div class="project-name">PROJECT NAME</div><p class="project-text">Duis aute irure dolor in reprehenderit in voluptate velit esse cillum dolore eu fugiat nulla pariatur. Excepteur sint occaecat ....</p></div>
  </article>
  <article class="abs project" style="left:241px; top:560px; width:193px; height:200px;">
    <div class="project-photo" role="img" aria-label="Multi-storey beige residential apartment complex under a deep blue sky" style="height:126px; background:linear-gradient(180deg,#1a56b0 0%,#4a7fc8 28%,#ddd7cb 42%,#c7bba7 65%,#a89a84 85%,#6f7a5a 100%);"></div>
    <div class="project-body" style="padding:10px 10px 0;"><div class="project-name" style="font-size:9.6px;">PROJECT NAME</div><p class="project-text" style="font-size:6.6px; line-height:11.5px;">Duis aute irure dolor in reprehenderit in voluptate velit esse cillum dolore eu fugiat nulla pariatur. Excepteur sint occaecat ....</p></div>
  </article>
  <div class="abs slider-btn" style="left:214px; top:626px;"><svg width="8" height="12" viewBox="0 0 8 12"><path d="M6 1L1.5 6 6 11" fill="none" stroke="#fff" stroke-width="1.5"/></svg></div>
  <div class="abs slider-btn" style="left:434px; top:626px;"><svg width="8" height="12" viewBox="0 0 8 12"><path d="M2 1l4.5 5L2 11" fill="none" stroke="#fff" stroke-width="1.5"/></svg></div>
</section>

<section>
  <h2 class="abs section-title" style="top:797px; gap:22px;"><span class="bars"><i></i><i></i><i></i></span>OUR PEOPLE<span class="bars"><i></i><i></i><i></i></span></h2>

  <article class="abs person" style="left:55px; top:838px;">
    <div class="person-photo" role="img" aria-label="Portrait of team member Mara, dimmed behind her bio" style="background:linear-gradient(180deg,#3b3634 0%,#453a35 55%,#6a3a2c 85%,#7e4330 100%);"></div>
    <p class="abs person-bio">Duis aute irure dolor in reprehenderit in voluptate velit esse cillum dolore eu fugiat nulla pariatur. Excepteur sint occaecat cupidatat non proident, sunt in culpa qui officia deserunt mollit anim id est laborum.</p>
    <div class="abs person-social">
      <span style="background:var(--teal);"><svg width="8" height="6" viewBox="0 0 8 6"><rect x=".5" y=".5" width="7" height="5" fill="none" stroke="#fff" stroke-width=".9"/><path d="M.5 .5L4 3.3 7.5 .5" fill="none" stroke="#fff" stroke-width=".9"/></svg></span>
      <span style="background:var(--green);"><svg width="8" height="8" viewBox="0 0 10 10"><path d="M3 2.3l1 1.2-.6.8c.4.9 1.1 1.6 2 2l.8-.6 1.2 1-.6 1c-2.6-.3-4.4-2.2-4.7-4.8z" fill="#fff"/></svg></span>
      <span style="background:var(--slate);"><svg width="6" height="8" viewBox="0 0 6 8"><path d="M3 7.6C1.2 5.4.5 4.2.5 3a2.5 2.5 0 015 0c0 1.2-.7 2.4-2.5 4.6z" fill="#fff"/><circle cx="3" cy="3" r=".9" fill="#3f4a55"/></svg></span>
      <span style="background:var(--grey);"><svg width="8" height="8" viewBox="0 0 8 8"><path d="M1.5 4h5M4.5 2l2 2-2 2" fill="none" stroke="#fff" stroke-width="1.1"/></svg></span>
    </div>
    <div class="person-name" style="background:var(--green);">MARA</div>
  </article>
  <article class="abs person" style="left:201px; top:838px;">
    <div class="person-photo" role="img" aria-label="Portrait of team member Tessa" style="background:radial-gradient(ellipse 45% 40% at 50% 40%,#d9a58a 0%,#b98a70 55%,rgba(0,0,0,0) 100%),linear-gradient(180deg,#dcdad8 0%,#c9c5c2 60%,#6a8a92 85%,#5a7880 100%);"></div>
    <div class="person-name" style="background:var(--teal);">TESSA</div>
  </article>
  <article class="abs person" style="left:347px; top:838px;">
    <div class="person-photo" role="img" aria-label="Portrait of team member Lucas" style="background:radial-gradient(ellipse 45% 40% at 50% 42%,#d49a78 0%,#b77f62 55%,rgba(0,0,0,0) 100%),linear-gradient(180deg,#e8e8e8 0%,#dcdcdc 60%,#2f2f31 85%,#262628 100%);"></div>
    <div class="person-name" style="background:var(--slate);">LUCAS</div>
  </article>
  <article class="abs person" style="left:494px; top:838px;">
    <div class="person-photo" role="img" aria-label="Portrait of team member Owen" style="background:radial-gradient(ellipse 42% 40% at 50% 42%,#e0b298 0%,#c99a80 55%,rgba(0,0,0,0) 100%),linear-gradient(180deg,#e6e6e6 0%,#dedede 65%,#e8ebf2 85%,#d6dbe6 100%);"></div>
    <div class="person-name" style="background:var(--grey);">OWEN</div>
  </article>
</section>

<section>
  <div class="abs newsletter"></div>
  <h2 class="abs section-title" style="top:1040px;"><span class="bars"><i></i><i></i><i></i></span>NEWSLETTER SUBSCRIBE<span class="bars"><i></i><i></i><i></i></span></h2>
  <div class="abs email-field">ENTER EMAIL ID
    <svg width="8" height="6" viewBox="0 0 8 6"><rect x=".5" y=".5" width="7" height="5" fill="none" stroke="#3f4a55" stroke-width=".9"/><path d="M.5 .5L4 3.3 7.5 .5" fill="none" stroke="#3f4a55" stroke-width=".9"/></svg>
  </div>
  <div class="abs btn-subscribe">SUBSCRIBE</div>
</section>

<footer>
  <div class="abs footer-brand"><span class="brand-square"></span><span class="brand-name">MERIDIAN CREST<br>ADVISERS</span></div>
  <nav class="abs footer-links"><span>Home</span><span>About Us</span><span>Recent Projects</span><span>Our People</span><span>Subscribe</span><span>Contact Us</span></nav>
  <p class="abs footer-copy">© 2017 .www.meridiancrest.com &nbsp;|&nbsp; All Rights Reserved.</p>
</footer>

</body>
</html>
```